Poster Needed for Church Conference

I need a poster for a weekend conference at my church. Looking to attract as many people as possible. We are a church in the suburbs of Houston. This is mainly for our own church members but we are opening it up to outside church members.

Please see previous design from last conference and all other graphic work that can (doesn't need to be) included.

Target Market(s)

It's targeted for all people. But our main audience is families. around the age of 30 should be main target.

Industry/Entity Type

Non-Profit

Font styles to use
Serif
Sans Serif

Colors

Designer to choose colors to be used in the design.

Requirements
Must have
• 11x17 design with ability to shrink and blow up. but ideally for 11x17
• Content and wording:
• "Rooted Lantern Conference: Bridging the gap between generations and passing on our deepest beliefs and values."
• Featuring Dr. Glen Marlowe. Author of "The Map of Q9"
• Aug 25-26: Friday 8-10 pm, Saturday 4-8 pm
• Cost Adults $15/Children $5: Covers admission to all sessions and workshops, refreshments and Saturday dinner. *kids 5 and under free
• Childcare provided for all sessions. "
• Please use church logo and address on flyer: 4312 Orchard Bend, Missouri City, TX 77512
Nice to have
• Ideally it will be designed so that we can crop a 16:9 pp announcement slide and header for our website.
Should not have
• anything offensive

```html
<!DOCTYPE html>
<html lang="en">
<head>
<meta charset="utf-8">
<title>Rooted Lantern Conference Poster</title>
<link href="https://fonts.googleapis.com/css2?family=Montserrat:wght@300;400;600;700;800&family=Oswald:wght@500;600&display=swap" rel="stylesheet">
<style>
  :root {
    --green: #3fae49;
    --ink: #111111;
    --grey: #4a4a4a;
    --light-grey: #6d6d6d;
    --paper: #ffffff;
    --backdrop: #e9e9e9;
  }
  * { margin: 0; padding: 0; box-sizing: border-box; }
  html, body { width: 1200px; height: 1200px; overflow: hidden; background: var(--backdrop); }
  .poster {
    position: absolute; left: 231px; top: 30px; width: 738px; height: 1140px;
    background: var(--paper); overflow: hidden;
    font-family: "Montserrat", sans-serif;
    box-shadow: 0 6px 24px rgba(0,0,0,0.12);
  }
  .hero-photo {
    position: absolute; left: 0; top: 0; width: 100%; height: 620px;
    background:
      linear-gradient(180deg, rgba(255,255,255,0) 55%, #ffffff 100%),
      radial-gradient(ellipse at 50% 25%, #fbfbfb 0%, #ececec 55%, #dedede 100%);
  }
  .abs { position: absolute; }
  .title { left: 0; width: 100%; text-align: center; font-weight: 800; line-height: 1; white-space: nowrap; }
  .title-top { top: 101px; color: var(--green); font-size: 62px; letter-spacing: -0.5px; }
  .title-bottom { top: 172px; color: var(--ink); font-size: 78px; letter-spacing: -0.5px; }
  .tagline {
    top: 266px; left: 0; width: 100%; text-align: center;
    font-size: 23px; font-weight: 600; color: var(--grey); line-height: 1.35; letter-spacing: 0.3px;
  }
  .featuring { left: 81px; top: 360px; font-size: 18px; font-weight: 700; color: var(--green); letter-spacing: 0.5px; }
  .speaker { left: 80px; top: 380px; font-size: 44px; font-weight: 700; color: var(--ink); white-space: nowrap; }
  .author-of { left: 80px; top: 428px; font-size: 35px; font-weight: 300; color: var(--light-grey); }
  .book-banner { left: 79px; top: 470px; width: 476px; height: 94px; }
  .book-title {
    left: 92px; top: 476px; font-size: 44px; color: #fff; font-weight: 400; line-height: 1;
    white-space: nowrap;
  }
  .book-title b { font-weight: 700; }
  .dates { font-family: "Oswald", sans-serif; left: 82px; line-height: 1; white-space: nowrap; }
  .date-range { top: 539px; font-size: 58px; font-weight: 600; color: var(--green); }
  .day { font-size: 36px; font-weight: 500; color: var(--ink); transform: scaleX(0.84); transform-origin: left; }
  .day-fri { top: 600px; }
  .day-sat { top: 640px; }
  .cost-lines { left: 0; top: 0; width: 738px; height: 1140px; pointer-events: none; }
  .cost-label { font-family: "Oswald", sans-serif; left: 150px; top: 690px; width: 74px; text-align: center; font-size: 30px; font-weight: 500; color: var(--ink); line-height: 1; transform: scaleX(0.88); }
  .price {
    width: 96px; height: 96px; border-radius: 50%; background: var(--green);
    display: flex; flex-direction: column; align-items: center; justify-content: center;
    color: #fff; line-height: 1; text-align: center;
  }
  .price-label { font-family: "Oswald", sans-serif; font-size: 20px; font-weight: 500; transform: scaleX(0.85); white-space: nowrap; }
  .price-amount { font-family: "Montserrat", sans-serif; font-size: 32px; font-weight: 800; margin-top: 2px; }
  .price-adult { left: 77px; top: 730px; }
  .price-child { left: 192px; top: 730px; }
  .cost-note { left: 82px; top: 843px; font-size: 13.5px; color: var(--grey); line-height: 1.32; white-space: nowrap; }
  .cost-note .free { color: var(--green); font-weight: 600; }
  .church-band {
    left: 0; top: 953px; width: 394px; height: 90px; background: var(--green);
    display: flex; align-items: center; padding-left: 80px; gap: 12px;
  }
  .church-dot { width: 14px; height: 14px; border-radius: 50%; background: #fff; flex: none; }
  .church-name { color: #fff; font-size: 19px; font-weight: 600; line-height: 1.2; }
  .address { left: 79px; top: 1064px; font-size: 18px; font-weight: 700; color: var(--grey); line-height: 1.3; font-style: normal; }
  .book-cover { left: 0; top: 0; width: 738px; height: 1140px; }
</style>
</head>
<body>
  <main class="poster">
    <div class="hero-photo" role="img" aria-label="Soft, bright blurred photo of a church sanctuary with tall arched windows"></div>

    <svg class="abs book-cover" viewBox="0 0 738 1140" role="img" aria-label="Photo of the book “The Map of Q9” by Dr. Glen Marlowe, white cover with green title">
      <defs>
        <linearGradient id="coverTone" x1="0" y1="0" x2="1" y2="1">
          <stop offset="0" stop-color="#f7f7f7"/>
          <stop offset="0.5" stop-color="#e2e2e2"/>
          <stop offset="0.8" stop-color="#cfe9d2"/>
          <stop offset="1" stop-color="#f0f0f0"/>
        </linearGradient>
      </defs>
      <polygon points="331,691 691,605 682,989 389,1094" fill="url(#coverTone)"/>
    </svg>

    <h1 class="abs title title-top">ROOTED LANTERN</h1>
    <div class="abs title title-bottom">CONFERENCE</div>
    <p class="abs tagline">Bridging the gap between generations and<br>passing on our deepest</p>

    <div class="abs featuring">FEATURING</div>
    <div class="abs speaker">Dr. Glen Marlowe.</div>
    <div class="abs author-of">Author of</div>

    <svg class="abs book-banner" viewBox="0 0 476 94" aria-hidden="true">
      <polygon points="0,0 458,0 458,56 474,93 418,56 0,56" fill="var(--green)"/>
    </svg>
    <div class="abs book-title">“The <b>Map</b> of <b>Q9</b>”</div>

    <div class="abs dates date-range">AUG 25-26</div>
    <div class="abs dates day day-fri">FRIDAY 8-10 PM</div>
    <div class="abs dates day day-sat">SATURDAY 4-8 PM</div>

    <svg class="abs cost-lines" viewBox="0 0 738 1140" aria-hidden="true">
      <polyline points="125,730 125,706 154,706" fill="none" stroke="var(--ink)" stroke-width="2"/>
      <polyline points="220,706 240,706 240,730" fill="none" stroke="var(--ink)" stroke-width="2"/>
    </svg>
    <div class="abs cost-label">COST:</div>
    <div class="abs price price-adult"><div class="price-label">ADULTS</div><div class="price-amount">$15</div></div>
    <div class="abs price price-child"><div class="price-label">CHILDREN</div><div class="price-amount">$5</div></div>

    <p class="abs cost-note">Covers admission to all sessions<br>and workshops, refreshments and<br>Saturday dinner.<br><span class="free">*kids 5 and under free</span><br>Childcare provided for all sessions.</p>

    <div class="abs church-band">
      <span class="church-dot"></span>
      <span class="church-name">Cedar Hollow<br>Community Church</span>
    </div>

    <address class="abs address">4312 Orchard Bend,<br>Missouri City,TX 77512</address>
  </main>
</body>
</html>
```